Hot Dog Menu 1

Web, TV, and print menu design project by 1) digitize or draw from a hand drawn menu, 2) make it available in 18 x 48 (in) for a print, 3) make it available to 1920 x 1080 (px) for a TV / USB, 3) make it available in two brand (logo provided). Attached files description: DPHD menu is the one we drew, Menu1 is the menu used by one of our competitor which we like ours to be like. Logo (Tolli Tolli) is the second brand we are about to launch. Daepung Hot Dog logo, you already have that from the previous project. The project is to create two identical menu board, one for Daepung and the other one is for Tolli Tolli to be displayed on TV (via USB), and to be printed on 18 x 48 prints. If you are interested to work on this project, please let me know.

```html
<!DOCTYPE html>
<html lang="en">
<head>
<meta charset="utf-8">
<title>Tolli Tolli – Hot Dog Menu</title>
<link rel="stylesheet" href="https://fonts.googleapis.com/css2?family=Lexend:wght@400;500&family=Oswald:wght@700&display=swap">
<style>
  :root {
    --board: #1c1c1c;
    --board-light: #2c2c2c;
    --orange: #f7941d;
    --frame: #b8762a;
    --text: #ffffff;
    --sausage-a: #e07a2e;
    --sausage-b: #a8431a;
    --smoked-a: #7a3a1c;
    --smoked-b: #3d1a0c;
    --rice-a: #b8431e;
    --rice-b: #5c1a0c;
    --ham-a: #f2b8b4;
    --ham-b: #9a3f20;
  }
  * { margin: 0; padding: 0; box-sizing: border-box; }
  html, body { width: 1200px; height: 600px; overflow: hidden; }
  body {
    background: radial-gradient(ellipse at 50% 45%, var(--board-light), var(--board) 75%);
    font-family: "Lexend", sans-serif;
    color: var(--text);
    position: relative;
  }
  .frame-line { position: absolute; background: var(--frame); }
  .frame-top-left { left: 36px; top: 50px; width: 318px; height: 1px; }
  .frame-top-right { left: 860px; top: 50px; width: 306px; height: 1px; }
  .frame-left { left: 36px; top: 50px; width: 1px; height: 506px; }
  .frame-right { left: 1166px; top: 50px; width: 1px; height: 506px; }
  .frame-bottom-left { left: 36px; top: 556px; width: 220px; height: 1px; }
  .frame-bottom-right { left: 944px; top: 556px; width: 222px; height: 1px; }

  .brand-name {
    position: absolute; left: 356px; top: 43px; width: 100px;
    text-align: center;
    font-family: "Lexend", sans-serif; font-weight: 500; font-size: 18px;
    line-height: 1; color: var(--text);
  }
  .menu-title {
    position: absolute; left: 466px; top: 24px;
    font-family: "Oswald", sans-serif; font-weight: 700;
    font-size: 62px; line-height: 1; color: var(--orange);
    letter-spacing: -0.5px;
  }

  .menu-item { position: absolute; display: flex; align-items: center; }
  .item-photo { width: 112px; height: 76px; border-radius: 22px; flex: none; }
  .item-name {
    margin-left: 44px; font-weight: 500; font-size: 18px; line-height: 1.25;
  }
  .photo-sausage { background: linear-gradient(160deg, var(--sausage-a), var(--sausage-b)); }
  .photo-smoked { background: linear-gradient(160deg, var(--smoked-a), var(--smoked-b)); height: 50px; }
  .photo-rice { background: linear-gradient(90deg, var(--rice-a), var(--rice-b)); height: 52px; }
  .photo-ham { background: linear-gradient(120deg, var(--ham-b), var(--ham-a)); height: 60px; border-radius: 30px; }

  .col-1 { left: 75px; }
  .col-2 { left: 442px; }
  .col-3 { left: 815px; }
  .row-1 { top: 160px; }
  .row-2 { top: 282px; }
  .row-3 { top: 400px; }

  .menu-note {
    position: absolute; left: 0; width: 1200px; top: 546px;
    text-align: center; font-size: 13px; line-height: 20px; font-weight: 400;
  }
  .menu-note strong { font-weight: 500; }
</style>
</head>
<body>
  <div class="frame-line frame-top-left"></div>
  <div class="frame-line frame-top-right"></div>
  <div class="frame-line frame-left"></div>
  <div class="frame-line frame-right"></div>
  <div class="frame-line frame-bottom-left"></div>
  <div class="frame-line frame-bottom-right"></div>

  <p class="brand-name">Tolli Tolli</p>
  <h1 class="menu-title">HOT DOG MENU</h1>

  <div class="menu-item col-1 row-1">
    <div class="item-photo photo-sausage" role="img" aria-label="Grilled pork and beef sausages"></div>
    <p class="item-name">Pork and<br>beef sausage</p>
  </div>
  <div class="menu-item col-1 row-2">
    <div class="item-photo photo-sausage" role="img" aria-label="Grilled beef sausages"></div>
    <p class="item-name">Beef sausage</p>
  </div>
  <div class="menu-item col-1 row-3">
    <div class="item-photo photo-rice" role="img" aria-label="Glazed rice cakes on a skewer"></div>
    <p class="item-name">Rice cake</p>
  </div>

  <div class="menu-item col-2 row-1">
    <div class="item-photo photo-smoked" role="img" aria-label="Long thin smoked sausages"></div>
    <p class="item-name">Pork and<br>beef&nbsp; mozzarila<br>sausage</p>
  </div>
  <div class="menu-item col-2 row-2">
    <div class="item-photo photo-sausage" role="img" aria-label="Curved grilled beef sausages"></div>
    <p class="item-name">Beef sausage<br>potatoes</p>
  </div>
  <div class="menu-item col-2 row-3">
    <div class="item-photo photo-ham" role="img" aria-label="Sliced mozzarella sausage"></div>
    <p class="item-name">Mozzarila</p>
  </div>

  <div class="menu-item col-3 row-1">
    <div class="item-photo photo-sausage" role="img" aria-label="Grilled cheddar pork and beef sausages"></div>
    <p class="item-name">Cheddar Pork and<br>beef&nbsp; sausage</p>
  </div>
  <div class="menu-item col-3 row-2">
    <div class="item-photo photo-sausage" role="img" aria-label="Grilled mozzarella pork and beef sausages"></div>
    <p class="item-name">Mozzarila Pork and<br>beef sausage</p>
  </div>
  <div class="menu-item col-3 row-3">
    <div class="item-photo photo-ham" role="img" aria-label="Sliced mozzarella cheddar sausage"></div>
    <p class="item-name">Mozzarila cheddar</p>
  </div>

  <p class="menu-note">Aditional Information <strong>+$1.00</strong> To Add Potatoes To Any Hot Dog.(Excluding The “premium”)</p>
</body>
</html>
```